Gentleman's grooming products require a business card

I need a business card that incorporates the logo [ or parts of ] that we had Art Parade design for us as uploaded.

We sell online, mens grooming products including moustache waxes, beard oils and shaving accessories.
We want a card that is classy, professional and a card that shouts mens products.

Target Market(s)

Young professional male market

Industry/Entity Type

Business

Contact Information for Business Card

Tess and Dulcie Abbott
Brass and Bristle
Purveyors of gentleman's stiffeners and grooming requisites
M :0491527306
E : tess@brassandbristle.com.au
E : dulcie@brassandbristle.com.au
E : sales@theboulevardpomade.com.au

W : www.brassandbristle.com.au

Requirements
Must have
• Class
Nice to have
• Professionalism

```html
<!DOCTYPE html>
<html lang="en">
<head>
<meta charset="utf-8">
<title>Brass and Bristle – Business Card</title>
<link rel="stylesheet" href="https://fonts.googleapis.com/css2?family=Pinyon+Script&family=Open+Sans:wght@400;600&display=swap">
<style>
  :root {
    --backdrop: #d4d4d4;
    --card: #ffffff;
    --ink: #111111;
    --muted: #555555;
    --accent: #f5a81c;
    --rule: #9a9a9a;
  }
  html, body {
    margin: 0;
    width: 1200px;
    height: 800px;
    overflow: hidden;
    background: var(--backdrop);
  }
  .business-card {
    position: absolute;
    left: 150px;
    top: 150px;
    width: 900px;
    height: 500px;
    background: var(--card);
    box-shadow: 0 6px 18px rgba(0,0,0,0.18);
    font-family: "Open Sans", Arial, sans-serif;
    overflow: hidden;
  }
  .brand-mark {
    position: absolute;
    right: 70px;
    top: 70px;
    display: flex;
    align-items: center;
    gap: 14px;
  }
  .brand-mark__square {
    width: 26px;
    height: 26px;
    background: var(--ink);
  }
  .brand-mark__name {
    font-weight: 600;
    font-size: 24px;
    color: var(--ink);
    letter-spacing: 0.5px;
  }
  .business-name {
    position: absolute;
    left: 48px;
    top: 118px;
    margin: 0;
    font-family: "Pinyon Script", cursive;
    font-weight: 400;
    font-size: 92px;
    line-height: 1;
    color: var(--ink);
  }
  .tagline {
    position: absolute;
    left: 205px;
    top: 232px;
    margin: 0;
    font-size: 17px;
    line-height: 1.2;
    color: var(--muted);
    text-align: center;
  }
  .divider {
    position: absolute;
    left: 420px;
    top: 262px;
    width: 470px;
    height: 2px;
    background: linear-gradient(to right, rgba(154,154,154,0), var(--rule) 35%, var(--rule) 80%, rgba(154,154,154,0));
  }
  .owners {
    position: absolute;
    left: 210px;
    top: 300px;
    margin: 0;
    font-size: 24px;
    font-weight: 400;
    color: var(--accent);
  }
  .contact-list {
    position: absolute;
    left: 212px;
    top: 336px;
    margin: 0;
    padding: 0;
    list-style: none;
  }
  .contact-list li {
    display: flex;
    align-items: center;
    gap: 10px;
    height: 27px;
    font-size: 17px;
    color: #333333;
  }
  .contact-list svg {
    width: 18px;
    height: 18px;
    flex: none;
  }
</style>
</head>
<body>
  <main class="business-card">
    <div class="brand-mark">
      <span class="brand-mark__square"></span>
      <span class="brand-mark__name">Brass and Bristle</span>
    </div>

    <h1 class="business-name">Brass and Bristle</h1>
    <p class="tagline">Purveyors of gentleman's stiffeners<br>and grooming requisites</p>
    <div class="divider"></div>

    <h2 class="owners">Tess and Dulcie Abbott</h2>
    <ul class="contact-list">
      <li>
        <svg viewBox="0 0 20 20" aria-hidden="true"><path fill="#f5a81c" d="M5 2l3 4-2 2c1 2.5 3.5 5 6 6l2-2 4 3-2 3C9 18 2 11 2 4z"/></svg>
        0491527306
      </li>
      <li>
        <svg viewBox="0 0 20 20" aria-hidden="true"><rect x="1" y="4" width="18" height="12" fill="#f5a81c"/><path d="M1 4l9 7 9-7" fill="none" stroke="#fff" stroke-width="1.5"/></svg>
        tess@brassandbristle.com.au
      </li>
      <li>
        <svg viewBox="0 0 20 20" aria-hidden="true"><rect x="1" y="4" width="18" height="12" fill="#f5a81c"/><path d="M1 4l9 7 9-7" fill="none" stroke="#fff" stroke-width="1.5"/></svg>
        dulcie@brassandbristle.com.au
      </li>
      <li>
        <svg viewBox="0 0 20 20" aria-hidden="true"><rect x="1" y="4" width="18" height="12" fill="#f5a81c"/><path d="M1 4l9 7 9-7" fill="none" stroke="#fff" stroke-width="1.5"/></svg>
        sales@theboulevardpomade.com.au
      </li>
      <li>
        <svg viewBox="0 0 20 20" aria-hidden="true"><circle cx="10" cy="10" r="8.5" fill="#f5a81c"/><path d="M1.5 10h17M10 1.5c-4 4-4 13 0 17M10 1.5c4 4 4 13 0 17" fill="none" stroke="#fff" stroke-width="1.2"/></svg>
        www.brassandbristle.com.au
      </li>
    </ul>
  </main>
</body>
</html>
```